Relaunch website https://dancepastdawn.de/

We are looking for creative minds to relaunch the website for our new musical “Dance past dawn” (www.dancepastdawn.de). The aim is to convey the full emotional power, spine-tingling intensity, and spirit of empowerment of this unique production.

The site should make the emotional depth and power of the musical come to life - not merely by describing it, but by letting people feel it. In accordance with our marketing philosophy: "Show, don't tell"—we tell the story, rather than simply promoting the musical.

The website should be responsive, offer intuitive navigation and be in accordance with the design guidelines. Please design the website with the compatibility of a specific WordPress theme in mind (in the best case choose from a big enterprise theme such as avada, enfold or divi).

Design specifications:
Primary color: Pink (R224 / G51 / B151)
Secondary color: yellow (R255 / G221 / B0)
Tertiary color: black (R29 / G29 / B27)
Font-Headline: Tungsten
Font body: DIN 1451 LT Pro
Background texture: Grunge

In addition to the main page, the following subpages will be relevant:
OURtale, The Musical, Cast & Team, Tickets, Plan your visit, Corporate events, Press, FAQ, Coupon, News

The winner will be selected according to the following criteria: creativity, user guidance, technical feasibility and compliance with the style guide. Also based on your unique ideas! We know the briefing is super specific but please let your ideas and feedback flow.

We have uploaded a detailed briefing document (including the CI) in German and English as well as the logos. You can use all available graphics from the current website and socials if needed for your pitch. Please design at least the following pages:
- Home (briefing included)
- OURTale (be creative - no specific briefing)
- Ticketing (separate briefing included)
- Corporate events (separate briefing included)
- Plan your visit (separate briefing included)
- News (be creative - no specific briefing)

If you have any questions, please contact marla.fenwick@dosuvel-entertainment.

We would love to give you more time for your designs!

Target Market(s)

Germany

Industry/Entity Type

Musical & Entertainment

Number of Pages Required

5+ page

Font styles to use
Other font styles liked:
• Headline: Tungsten & Body: DIN 1451 LT Pro

Colors
FFF300
FFF600
FEFA6F
FFFEC7
FFFEE8
E54698
E96AAD
F1A4CE
F9D9EA
FCEFF6

Requirements
Must have
• See briefing
Nice to have
• See briefing
Should not have
• See briefing

```html
<!DOCTYPE html>
<html lang="en">
<head>
<meta charset="utf-8">
<title>Dance past dawn – Das Musical</title>
<link href="https://fonts.googleapis.com/css2?family=Bebas+Neue&family=Poppins:wght@400;500&display=swap" rel="stylesheet">
<style>
:root{
  --pink:#e03397;
  --yellow:#ffdd00;
  --ink:#0d0809;
  --panel:#1d1d1b;
  --white:#f4f1ee;
  --muted:#cfc9c6;
  --line:#4a4446;
}
*{box-sizing:border-box;margin:0;padding:0}
html,body{width:1200px;height:2820px;overflow:hidden;background:var(--ink);color:var(--white)}
body{position:relative;font-family:"Poppins",sans-serif}
.display{font-family:"Bebas Neue",sans-serif;font-weight:400;line-height:1;letter-spacing:0}
.pink{color:var(--pink)}
.yellow{color:var(--yellow)}
em{font-style:normal}
.abs{position:absolute}
.btn{position:absolute;display:flex;align-items:center;justify-content:center;gap:12px;font-family:"Bebas Neue",sans-serif;font-size:16px;letter-spacing:.3px;color:var(--white);text-decoration:none;white-space:nowrap}
.btn-solid{background:var(--pink)}
.btn-outline{border:1px solid var(--white)}
.btn-gold{border:1px solid var(--yellow);color:var(--yellow)}
.arrow{width:30px;height:8px}
.copy{font-size:15px;line-height:22px;color:var(--white)}

/* header */
.site-header{position:absolute;left:0;top:0;width:1200px;height:73px;background:var(--ink)}
.brand{position:absolute;display:flex;align-items:center;gap:10px}
.brand-mark{width:14px;height:14px;background:var(--pink)}
.brand-name{font-family:"Bebas Neue",sans-serif;color:var(--white);font-size:30px;line-height:1;white-space:nowrap}
.main-nav{position:absolute;left:392px;top:27px;display:flex;gap:26px;font-family:"Bebas Neue",sans-serif;font-size:15px}
.main-nav a{color:var(--white);text-decoration:none}

/* hero */
.hero-photo{position:absolute;left:473px;top:73px;width:727px;height:522px;
  background:linear-gradient(90deg,rgba(13,8,9,.9) 0%,rgba(13,8,9,.2) 30%,transparent 55%),
  radial-gradient(ellipse at 75% 55%,#8fb3bd 0%,#4f6d73 30%,transparent 60%),
  radial-gradient(ellipse at 40% 35%,#7a4b52 0%,#3a2327 40%,#140c0d 80%)}
.hero-title{position:absolute;left:50px;top:165px;font-size:86px}
.hero-title span{display:block;height:90px;white-space:nowrap}

/* story */
.story-photo{position:absolute;left:0;top:601px;width:820px;height:476px;
  background:linear-gradient(90deg,transparent 40%,rgba(13,8,9,.85) 75%,var(--ink) 100%),
  radial-gradient(ellipse at 30% 70%,#5d7fa6 0%,#3b4d6b 35%,transparent 65%),
  radial-gradient(ellipse at 40% 20%,#9b8468 0%,#4c3e31 45%,#1c1514 90%)}
.timeline{position:absolute;left:586px;top:697px}
.timeline-item{position:absolute;left:0;width:230px}
.timeline-year{font-family:"Bebas Neue",sans-serif;font-size:24px;color:var(--yellow);line-height:1}
.timeline-text{font-size:15px;line-height:22px;margin-top:2px;white-space:nowrap}
.timeline-text.small{font-family:"Bebas Neue",sans-serif;font-size:13px}
.section-title{position:absolute;font-size:80px;white-space:nowrap}
.quote-box{position:absolute;left:981px;top:936px;width:219px;height:110px;background:var(--panel);padding:24px 0 0 30px;font-family:"Bebas Neue",sans-serif;font-size:24px;line-height:34px;white-space:nowrap}

/* musical */
.musical-photo{position:absolute;left:0;top:1077px;width:1200px;height:520px;
  background:radial-gradient(ellipse at 60% 55%,#b1161d 0%,#6d0d12 35%,#2a0608 65%,#140506 100%)}
.feel-lines{position:absolute;left:802px;top:1384px;font-size:54px}
.feel-lines span{display:block;height:61px;white-space:nowrap}

/* cast */
.cast-card{position:absolute;top:1692px;width:170px}
.cast-photo{width:170px;height:239px}
.cast-name{font-family:"Bebas Neue",sans-serif;font-size:23px;margin-top:12px;line-height:1;white-space:nowrap}
.slider-btn{position:absolute;top:1984px;width:34px;height:34px}

/* live */
.benefits{position:absolute;left:563px;top:2086px;list-style:none;font-size:15px;line-height:30px;color:var(--muted)}
.eyebrow{position:absolute;font-family:"Bebas Neue",sans-serif;font-size:19px;color:var(--pink)}
.card-title{position:absolute;font-size:55px;white-space:nowrap}

/* footer */
.footer-rule{position:absolute;left:0;top:2615px;width:1200px;height:1px;background:var(--line)}
.subscribe{position:absolute;left:423px;top:2700px;display:flex}
.subscribe-field{width:209px;height:46px;border:1px solid var(--line);font-family:"Bebas Neue",sans-serif;font-size:15px;color:#8d8688;padding:14px 9px}
.subscribe-btn{width:52px;height:46px;background:var(--pink);display:flex;align-items:center;justify-content:center}
.quick-links{position:absolute;left:981px;top:2706px;list-style:none;font-family:"Bebas Neue",sans-serif;font-size:14px;line-height:27px}
</style>
</head>
<body>

<header class="site-header">
  <div class="brand" style="left:50px;top:22px">
    <span class="brand-mark"></span>
    <span class="brand-name">Dance past dawn</span>
  </div>
  <nav class="main-nav">
    <a href="#">History</a><a href="#">The Musical</a><a href="#">Cast &amp; Team</a><a href="#">Tickets</a><a href="#">Plan Your Visit</a><a href="#">FAQ</a>
  </nav>
  <a class="btn btn-solid" href="#" style="left:1017px;top:13px;width:133px;height:46px">Get Tickets</a>
</header>

<section class="hero">
  <div class="hero-photo" role="img" aria-label="Older woman signing a football for fans in front of a theatre"></div>
  <h1 class="hero-title display">
    <span>They said <em class="pink">No.</em></span>
    <span>She kicked <em class="yellow">anyway.</em></span>
  </h1>
  <p class="copy abs" style="left:50px;top:363px;width:570px">A powerful musical inspired by the women who challenged expectations, broke barriers, and rewrote history through football.</p>
  <a class="btn btn-solid" href="#" style="left:50px;top:424px;width:169px;height:47px">Watch the Story</a>
  <a class="btn btn-outline" href="#" style="left:235px;top:424px;width:171px;height:47px">Book Tickets</a>
</section>

<section class="story">
  <div class="story-photo" role="img" aria-label="Archive photo of a women's team celebrating with trophies"></div>
  <div class="timeline">
    <div class="timeline-item" style="top:0"><div class="timeline-year">1970s</div><div class="timeline-text">Dreams met resistance.</div></div>
    <div class="timeline-item" style="top:99px"><div class="timeline-year">1978</div><div class="timeline-text">A team found its voice.</div></div>
    <div class="timeline-item" style="top:198px"><div class="timeline-year">1981</div><div class="timeline-text">History stepped onto the fifld.</div></div>
    <div class="timeline-item" style="top:297px"><div class="timeline-year">Today</div><div class="timeline-text small">Their legacy inspired generations.</div></div>
  </div>
  <h2 class="section-title display" style="left:831px;top:704px">Our <span class="pink">Tale</span></h2>
  <p class="copy abs" style="left:831px;top:810px;width:270px">There were women who refused to accept the rules they were given. This is their journey of courage, resilience, and determination.</p>
  <a class="btn btn-solid" href="#" style="left:831px;top:969px;width:148px;height:46px">Explore the Journey</a>
  <div class="quote-box">Before the spotlight.<br>Before the applause.</div>
</section>

<section class="musical">
  <div class="musical-photo" role="img" aria-label="Hand on a sound mixing desk lit in red stage light"></div>
  <h2 class="section-title display" style="left:50px;top:1150px">The <span class="yellow">Musical</span></h2>
  <p class="copy abs" style="left:50px;top:1241px;width:430px">An unforgettable stage experience that blends music, emotion, and the true spirit of teamwork.</p>
  <a class="btn btn-outline" href="#" style="left:50px;top:1334px;width:169px;height:46px">Discover the Show
    <svg class="arrow" viewBox="0 0 30 8"><path d="M0 4H28M24 1l4 3-4 3" stroke="#f4f1ee" fill="none"/></svg></a>
  <div class="feel-lines display">
    <span>Feel every <em class="pink">victory.</em></span>
    <span>Feel every <em class="yellow">setback.</em></span>
    <span>Feel every <em class="pink">moment.</em></span>
  </div>
</section>

<section class="cast">
  <h2 class="display abs" style="left:50px;top:1671px;font-size:90px;line-height:88px">Cast &amp;<br>Team</h2>
  <p class="copy abs" style="left:50px;top:1857px;width:360px">Meet the performers, creators, and visionaries bringing this extraordinary story to life.</p>
  <a class="btn btn-outline" href="#" style="left:50px;top:1930px;width:169px;height:47px">Meet the Cast
    <svg class="arrow" viewBox="0 0 30 8"><path d="M0 4H28M24 1l4 3-4 3" stroke="#f4f1ee" fill="none"/></svg></a>
  <div class="cast-card" style="left:423px"><div class="cast-photo" role="img" aria-label="Portrait of cast member Lena Marquardt" style="background:linear-gradient(160deg,#b9523f,#8a3427 60%,#d3786a)"></div><div class="cast-name">Lena Marquardt</div></div>
  <div class="cast-card" style="left:609px"><div class="cast-photo" role="img" aria-label="Portrait of cast member Lena Marquardt" style="background:linear-gradient(160deg,#dcd8d4,#b99a85 55%,#2a2120)"></div><div class="cast-name">Lena Marquardt</div></div>
  <div class="cast-card" style="left:795px"><div class="cast-photo" role="img" aria-label="Portrait of cast member Carla Venner" style="background:linear-gradient(160deg,#3a3532,#8a4a2c 50%,#1c1717)"></div><div class="cast-name">Carla Venner</div></div>
  <div class="cast-card" style="left:981px"><div class="cast-photo" role="img" aria-label="Portrait of cast member Mira Solberg" style="background:linear-gradient(160deg,#bdb7b2,#6a4a3c 50%,#211918)"></div><div class="cast-name">Mira Solberg</div></div>
  <svg class="slider-btn" style="left:1073px" viewBox="0 0 34 34"><circle cx="17" cy="17" r="16" fill="none" stroke="#6f6869"/><path d="M25 17H9M14 12l-5 5 5 5" stroke="#8d8688" fill="none" stroke-width="1.5"/></svg>
  <svg class="slider-btn" style="left:1116px" viewBox="0 0 34 34"><circle cx="17" cy="17" r="16" fill="none" stroke="#f4f1ee"/><path d="M9 17H25M20 12l5 5-5 5" stroke="#f4f1ee" fill="none" stroke-width="1.5"/></svg>
</section>

<section class="live">
  <h2 class="display abs" style="left:50px;top:2087px;font-size:84px;white-space:nowrap">Live the Moment</h2>
  <ul class="benefits"><li>Limited Performances</li><li>Award-Winning Production</li><li>An Experience To Remember</li></ul>
  <a class="btn btn-solid" href="#" style="left:895px;top:2105px;width:168px;height:46px">Find Your Date
    <svg class="arrow" viewBox="0 0 30 8"><path d="M0 4H28M24 1l4 3-4 3" stroke="#f4f1ee" fill="none"/></svg></a>
</section>

<section class="cards">
  <div class="eyebrow" style="left:50px;top:2255px">For Organisations</div>
  <h2 class="card-title display" style="left:50px;top:2285px">Inspire Your People</h2>
  <p class="abs" style="left:50px;top:2360px;font-size:14px;line-height:22px">A story about leadership, teamwork, courage,<br>and overcoming challenges together.<br>Perfect for corporate events and group experiences.</p>
  <a class="btn btn-gold" href="#" style="left:50px;top:2435px;width:170px;height:46px">Learn More
    <svg class="arrow" viewBox="0 0 30 8"><path d="M0 4H28M24 1l4 3-4 3" stroke="#ffdd00" fill="none"/></svg></a>

  <div class="eyebrow" style="left:609px;top:2255px">Latest Updates</div>
  <h2 class="card-title display" style="left:609px;top:2285px">Stay Updated</h2>
  <p class="abs" style="left:609px;top:2360px;font-size:14px;line-height:22px">Go behind the scenes, meet the cast,<br>and stay connected with the latest<br>announcements.</p>
  <a class="btn btn-gold" href="#" style="left:609px;top:2435px;width:169px;height:46px">See More
    <svg class="arrow" viewBox="0 0 30 8"><path d="M0 4H28M24 1l4 3-4 3" stroke="#ffdd00" fill="none"/></svg></a>
</section>

<footer class="site-footer">
  <div class="footer-rule"></div>
  <div class="brand" style="left:50px;top:2707px">
    <span class="brand-mark"></span>
    <span class="brand-name">Dance past dawn</span>
  </div>
  <div class="eyebrow" style="left:423px;top:2666px">Subscribe Us</div>
  <form class="subscribe">
    <div class="subscribe-field">Your Email Address</div>
    <div class="subscribe-btn"><svg width="22" height="14" viewBox="0 0 22 14"><path d="M1 7H20M14 1l6 6-6 6" stroke="#f4f1ee" fill="none" stroke-width="1.8"/></svg></div>
  </form>
  <div class="eyebrow" style="left:981px;top:2666px">Quick Links</div>
  <ul class="quick-links"><li>Contact Us</li><li>Privacy Policy</li><li>FAQ</li></ul>
</footer>

</body>
</html>
```